Brisa Pastry Mill Business card

We are empanada whole-sellers and I want a business card design with a picture of an empanada on it that also mentions first trial order FREE. our contact number 555-214-7093 our website www.brisapastry.example and business email Tobin@brisapastry.example

If you want any of our artwork please feel free to email me at the address above.

```html
<!DOCTYPE html>
<html lang="en">
<head>
<meta charset="utf-8">
<title>Brisa Pastry Mill Business Card</title>
<link href="https://fonts.googleapis.com/css2?family=Arvo:wght@400;700&family=Archivo:wght@800&display=swap" rel="stylesheet">
<style>
  :root {
    --backdrop: #928a8c;
    --mustard: #e9c94c;
    --cocoa: #3a2b1c;
    --paper: #ffffff;
    --pastry-light: #f0b070;
    --pastry-deep: #c8642a;
  }
  html, body { margin: 0; padding: 0; overflow: hidden; }
  body {
    width: 936px; height: 1200px;
    background: var(--backdrop);
    position: relative;
    font-family: "Arvo", serif;
  }
  .card {
    position: absolute;
    background: var(--paper);
    box-shadow: 0 6px 14px rgba(0,0,0,0.25);
    overflow: hidden;
  }
  .card-front { left: 171px; top: 196px; width: 590px; height: 367px; }
  .card-back  { left: 172px; top: 614px; width: 589px; height: 367px; }

  .front-field {
    position: absolute; left: 0; top: 0; width: 398px; height: 367px;
    background: var(--mustard);
  }
  .wordmark {
    position: absolute; text-align: center; color: var(--cocoa);
  }
  .wordmark-name {
    display: block; font-weight: 700; font-size: 62px; line-height: 1;
  }
  .wordmark-tagline {
    display: block; font-size: 13px; letter-spacing: 0.2px; margin-top: 10px;
  }
  .card-front .wordmark { left: 40px; top: 130px; width: 320px; }
  .card-back .wordmark { left: 0; top: 82px; width: 589px; }
  .card-back .wordmark-name { font-size: 70px; }
  .card-back .wordmark-tagline { font-size: 14px; }

  .photo {
    position: absolute; left: 409px; width: 173px;
  }
  .photo-filled { top: 8px; height: 128px;
    background: linear-gradient(160deg, var(--pastry-light), var(--pastry-deep) 60%, #8a4a2a); }
  .photo-spiral { top: 145px; height: 120px;
    background: radial-gradient(circle at 55% 55%, #f6c98c, #e08a40 55%, #b8561e); }

  .offer-ribbon { position: absolute; left: 358px; top: 254px; width: 225px; height: 105px; }
  .offer-text {
    position: absolute; left: 448px; top: 270px; width: 100px; height: 72px;
    color: var(--paper); font-weight: 700; line-height: 1;
  }
  .offer-num { position: absolute; left: 0; top: 0; font-size: 38px; }
  .offer-num sup { font-size: 10px; vertical-align: top; position: relative; top: -2px; }
  .offer-small { position: absolute; font-size: 15px; letter-spacing: 1px; white-space: nowrap; }
  .offer-small.first { top: 4px; left: 33px; }
  .offer-small.second { top: 23px; left: 31px; }
  .offer-big { position: absolute; left: 0; top: 43px; font-size: 31px; letter-spacing: 1.5px; }

  .contact-band { position: absolute; left: 0; top: 271px; width: 589px; height: 96px; }
  .phone-panel {
    position: absolute; left: 0; top: 0; width: 335px; height: 96px;
    background: var(--mustard);
  }
  .phone-number {
    position: absolute; left: 28px; top: 24px;
    font-family: "Archivo", sans-serif; font-weight: 800; font-size: 38px;
    color: var(--cocoa); text-shadow: 2px 2px 0 var(--paper); letter-spacing: -0.5px;
  }
  .web-panel {
    position: absolute; left: 338px; top: 0; width: 251px; height: 96px;
    background: var(--cocoa); color: var(--paper);
  }
  .web-line {
    position: absolute; left: 18px; font-weight: 700; font-size: 14px; white-space: nowrap;
  }
  .web-line.email { top: 24px; }
  .web-line.site { top: 50px; }
</style>
</head>
<body>
  <section class="card card-front">
    <div class="front-field"></div>
    <div class="wordmark">
      <span class="wordmark-name">Brisa</span>
      <span class="wordmark-tagline">MALAYSIAN &amp; THAI STREET FOOD</span>
    </div>
    <div class="photo photo-filled" role="img" aria-label="Photo of a halved empanada showing spiced meat filling"></div>
    <div class="photo photo-spiral" role="img" aria-label="Close-up photo of a flaky spiral-layered pastry"></div>
    <svg class="offer-ribbon" viewBox="0 0 225 105" aria-hidden="true">
      <polygon points="0,0 225,0 225,105 0,105 40,52" fill="var(--cocoa)"/>
      <polygon points="0,0 8,0 48,52 40,52" fill="#000" opacity="0.55"/>
    </svg>
    <div class="offer-text">
      <span class="offer-num">1<sup>st</sup></span>
      <span class="offer-small first">TRIAL</span>
      <span class="offer-small second">ORDER</span>
      <span class="offer-big">FREE</span>
    </div>
  </section>

  <section class="card card-back">
    <div class="wordmark">
      <span class="wordmark-name">Brisa</span>
      <span class="wordmark-tagline">MALAYSIAN &amp; THAI STREET FOOD</span>
    </div>
    <div class="contact-band">
      <div class="phone-panel">
        <span class="phone-number">555-214-7093</span>
      </div>
      <div class="web-panel">
        <span class="web-line email">Tobin@brisapastry.example</span>
        <span class="web-line site">www.brisapastry.example</span>
      </div>
    </div>
  </section>
</body>
</html>
```